Letterhead & Business Card Design Project

Use existing logo to create a new letterhead and business card design. Looking for something clean modern using color options of black, white and gray. The green from the logo may be used lightly as an accent color.

Target Market(s)

Professional business people

Industry/Entity Type

Business

Requirements
Must have
• Business card with front and back design using existing logo.
Nice to have
• Professional presentation
Clean look
Should not have
• No oil rigs, pumpjacks or clip art.

```html
<!DOCTYPE html>
<html lang="en">
<head>
<meta charset="utf-8">
<title>Ridgeline Exploration – Business Card</title>
<link rel="stylesheet" href="https://fonts.googleapis.com/css2?family=Questrial&display=swap">
<style>
  :root {
    --page-bg: #ececec;
    --front-center: #e6e6e6;
    --front-edge: #626262;
    --back-band: #3a3a3a;
    --back-panel: #4c4c4c;
    --back-panel-light: #575757;
    --logo-panel: #8a8a8a;
    --ink-dark: #1e1e1e;
    --ink-mid: #3a3a3a;
    --ink-light: #f2f2f2;
    --accent-green: #3ec13a;
  }
  * { box-sizing: border-box; margin: 0; padding: 0; }
  html, body { width: 854px; height: 1200px; overflow: hidden; }
  body {
    background: var(--page-bg);
    font-family: "Questrial", "Century Gothic", sans-serif;
    position: relative;
  }
  .card {
    position: absolute;
    width: 597px;
    height: 365px;
    box-shadow: 4px 5px 10px rgba(0,0,0,0.35);
  }
  .card-front {
    left: 134px; top: 168px;
    background: radial-gradient(ellipse 58% 68% at 50% 42%, var(--front-center) 0%, #bdbdbd 45%, var(--front-edge) 100%);
  }
  .brand-name {
    color: var(--ink-dark);
    letter-spacing: 0.08em;
    white-space: nowrap;
  }
  .card-front .brand-name {
    position: absolute;
    top: 150px; left: 0; width: 100%;
    text-align: center;
    font-size: 38px;
  }
  .card-front .website {
    position: absolute;
    top: 326px; left: 0; width: 100%;
    text-align: center;
    font-size: 13px;
    color: var(--ink-mid);
  }
  .card-back {
    left: 139px; top: 717px;
    background: var(--back-band);
  }
  .logo-panel {
    position: absolute;
    left: 0; top: 13px;
    width: 236px; height: 338px;
    background: var(--logo-panel);
  }
  .logo-panel .brand-name {
    position: absolute;
    top: 148px; left: 0; width: 100%;
    text-align: center;
    font-size: 19px;
  }
  .logo-panel .website {
    position: absolute;
    top: 310px; left: 0; width: 100%;
    text-align: center;
    font-size: 12px;
    color: var(--ink-dark);
  }
  .info-panel {
    position: absolute;
    left: 236px; top: 13px;
    width: 361px; height: 338px;
    background: linear-gradient(180deg, var(--back-panel-light) 0%, var(--back-panel) 100%);
    color: var(--ink-light);
  }
  .person-name {
    position: absolute;
    top: 144px; left: 0; width: 100%;
    text-align: center;
    font-size: 29px;
  }
  .person-title {
    position: absolute;
    top: 182px; left: 0; width: 100%;
    text-align: center;
    font-size: 16px;
    color: var(--accent-green);
  }
  .contact {
    position: absolute;
    left: 32px; top: 278px;
    width: 296px;
    font-size: 11.5px;
    line-height: 16px;
  }
  .contact-row { display: flex; justify-content: space-between; }
  .contact-row.right { justify-content: flex-end; }
</style>
</head>
<body>
  <section class="card card-front">
    <div class="brand-name">Ridgeline Exploration</div>
    <div class="website">www.ridgelineexploration.com</div>
  </section>

  <section class="card card-back">
    <div class="logo-panel">
      <div class="brand-name">Ridgeline Exploration</div>
      <div class="website">www.ridgelineexploration.com</div>
    </div>
    <div class="info-panel">
      <div class="person-name">Martin J Hale</div>
      <div class="person-title">Managing Member</div>
      <div class="contact">
        <div class="contact-row">4420 North Elm Ave Suite 210 Tulsa, Oklahoma 74135</div>
        <div class="contact-row"><span>Phone 918.555.0142</span><span>Fax 918.555.0143</span></div>
        <div class="contact-row right"><span>Cell 918.555.0178</span></div>
      </div>
    </div>
  </section>
</body>
</html>
```